Modernise Business Card

Our company has been operating for 10 years. With the start of the new decade we are looking to refresh our business card design. We manufacture a range of industrial product shipping to customers internationally. A copy of our current card, both sides, is attached. We are looking for a mature professional appearance.

```html
<!DOCTYPE html>
<html lang="en">
<head>
<meta charset="utf-8">
<title>Korvex Business Card</title>
<link href="https://fonts.googleapis.com/css2?family=Poppins:wght@400;500;700;800&display=swap" rel="stylesheet">
<style>
  :root {
    --stage: #2a2b2e;
    --brand-blue: #1ba7d9;
    --brand-blue-deep: #0b7cbc;
    --ink: #1f2022;
    --paper: #fbfcfd;
    --white: #ffffff;
  }
  html, body {
    margin: 0;
    width: 1200px;
    height: 900px;
    overflow: hidden;
    background: var(--stage);
    font-family: "Poppins", sans-serif;
  }
  .stage { position: relative; width: 1200px; height: 900px; }
  .card {
    position: absolute;
    width: 620px;
    height: 360px;
    border-radius: 22px;
    overflow: hidden;
    box-shadow: 0 18px 40px rgba(0,0,0,.45);
  }
  .card-front {
    left: 90px; top: 90px;
    background: linear-gradient(160deg, var(--brand-blue) 0%, var(--brand-blue-deep) 100%);
    color: var(--white);
  }
  .card-front .wordmark {
    position: absolute; left: 0; right: 0; top: 118px;
    text-align: center;
    font-weight: 800; font-size: 84px; line-height: 1;
    color: var(--white);
  }
  .card-front .website {
    position: absolute; left: 0; right: 0; top: 272px;
    text-align: center; font-size: 14px; letter-spacing: .3px;
  }
  .card-back {
    left: 490px; top: 450px;
    background: var(--paper);
    color: var(--ink);
  }
  .card-back .wordmark {
    position: absolute; left: 120px; top: 40px;
    font-weight: 800; font-size: 72px; line-height: 1;
    color: var(--brand-blue);
  }
  .identity {
    position: absolute; right: 310px; top: 140px;
    text-align: right;
  }
  .identity .name {
    font-weight: 700; font-size: 26px; line-height: 1.1; letter-spacing: .5px;
  }
  .identity .name .surname { color: var(--brand-blue); }
  .identity .tagline { font-size: 11.5px; margin-top: 4px; white-space: nowrap; }
  .contacts {
    position: absolute; right: 330px; top: 212px;
    text-align: right; font-size: 12.5px; line-height: 1.5;
    white-space: nowrap;
  }
  .contacts .label { color: var(--brand-blue); }
  .contacts .group + .group { margin-top: 12px; }
  .icons {
    position: absolute; left: 298px; top: 214px;
    display: flex; flex-direction: column; gap: 5px;
  }
  .icons svg { display: block; }
  .divider {
    position: absolute; left: 326px; top: 178px;
    width: 1.5px; height: 120px; background: var(--brand-blue);
  }
  .address {
    position: absolute; left: 340px; top: 180px;
    font-size: 12.5px; line-height: 1.45;
    font-style: normal; white-space: nowrap;
  }
</style>
</head>
<body>
<main class="stage">
  <section class="card card-front" aria-label="Card front">
    <div class="wordmark">Korvex</div>
    <div class="website">www.korvexfittings.com</div>
  </section>

  <section class="card card-back" aria-label="Card back">
    <div class="wordmark">Korvex</div>

    <div class="identity">
      <div class="name">EVAN <span class="surname">MARLOW</span></div>
      <div class="tagline">Hydraulic Adapters hose Fittings Quick Couplings</div>
    </div>

    <div class="contacts">
      <div class="group">
        <div><span class="label">China:</span> +86 130 5550 0142</div>
        <div><span class="label">Australia:</span> +61 400 555 019</div>
      </div>
      <div class="group">
        <div><span class="label">Email:</span> emarlow@korvexfittings.com</div>
        <div><span class="label">Web:</span> www.korvexfittings.com</div>
      </div>
    </div>

    <div class="icons">
      <svg class="icon-phone" width="14" height="18" viewBox="0 0 14 18" aria-hidden="true">
        <rect x="1.5" y="1" width="11" height="16" rx="2" fill="none" stroke="#1ba7d9" stroke-width="1.6"/>
        <circle cx="7" cy="14" r="1" fill="#1ba7d9"/>
      </svg>
      <div style="height:14px"></div>
      <svg class="icon-mail" width="16" height="12" viewBox="0 0 16 12" aria-hidden="true">
        <rect x="0" y="0" width="16" height="12" rx="1.5" fill="#1ba7d9"/>
        <path d="M1 1.5 L8 7 L15 1.5" fill="none" stroke="#fff" stroke-width="1.4"/>
      </svg>
      <svg class="icon-globe" width="14" height="14" viewBox="0 0 14 14" aria-hidden="true">
        <circle cx="7" cy="7" r="6" fill="none" stroke="#1ba7d9" stroke-width="1.6"/>
        <path d="M1 7 H13 M7 1 C4 4 4 10 7 13 M7 1 C10 4 10 10 7 13" fill="none" stroke="#1ba7d9" stroke-width="1.1"/>
      </svg>
    </div>

    <div class="divider" aria-hidden="true"></div>

    <address class="address">
      1208-3, Lian Fa Tower<br>
      77 Qingshan Road, Haishu District<br>
      Ningbo 315000 China
    </address>
  </section>
</main>
</body>
</html>
```